Parcel Badge Inc. NEED DESIGNS FOR THE HOLIDAY STICKERS

We need 6 designs for the HOLIDAY SET of Parcel Badges. I have attached some imagery that we like as well as the flagship pack of stickers that were also designed by you AWESOME DESIGNERS!! You are not limited to this imagery, it is only to show you what style we like but remember, YOU ARE THE ARTIST! Each design needs to have a "TO: & FROM:" for people to write in their name and the recipients name. We need designs for the following occasions:

1. HALLOWEEN
2. HAPPY HOLIDAYS (THANKSGIVING, CHRISTMAS, WINTER, LEAVES)
3. ST. PATRICK'S DAY
4. "LET'S CELEBRATE" PATRIOTIC THEME (JULY 4TH, VETERANS DAY, MEMORIAL DAY COMBINED)
5. HAPPY NEW YEAR
6. SUMMER THEME GENERIC

***these 6 designs must fit on one of die cut shapes which are included in the brief***

**PLEASE SUBMIT YOUR IDEA FOR AS MANY DESIGNS AS YOU CAN (PREFERABLY ALL 6). WE NEED 6 DESIGNS SO IF 4 OF YOURS ARE GOOD AND 2 OF ANOTHERS ARE GOOD, YOU WOULD WIN 1ST AND THEY WOULD WIN 2ND.

Font styles to use
Serif
Sans Serif
Decorative
Script

Requirements
Must have
• - lines for "to" and "from"
• - must fit on a die cut shape (provided)
• - must be FUN and colorful!!
Nice to have
• color, imagery, fun!

```html
<!DOCTYPE html>
<html lang="en">
<head>
<meta charset="utf-8">
<title>Parcel Badges – Happy Holidays Gift Sticker</title>
<link rel="stylesheet" href="https://fonts.googleapis.com/css2?family=Oleo+Script:wght@700&family=Mrs+Saint+Delafield&display=swap">
<style>
  :root {
    --page: #ffffff;
    --gold-light: #f3dc86;
    --gold-mid: #d9ad3c;
    --gold-deep: #b8862a;
    --rope: #7a4a14;
    --red: #a50a0a;
    --red-deep: #8c0606;
    --red-glow: #b81616;
    --label-white: #ffffff;
    --title-red: #c8161d;
    --ink-grey: #8a8a8a;
    --rule-grey: #b9b9b9;
  }
  html, body {
    margin: 0;
    padding: 0;
    width: 1200px;
    height: 1200px;
    overflow: hidden;
    background: var(--page);
  }
  .sticker {
    display: block;
    width: 1200px;
    height: 1200px;
  }
  .sticker__title {
    font-family: "Oleo Script", "Georgia", serif;
    font-weight: 700;
    font-style: italic;
    fill: var(--title-red);
  }
  .sticker__field-label {
    font-family: "Mrs Saint Delafield", "Brush Script MT", cursive;
    fill: var(--ink-grey);
  }
  .sticker__rule {
    stroke: var(--rule-grey);
    stroke-width: 1.2;
  }
</style>
</head>
<body>
<svg class="sticker" viewBox="0 0 1200 1200" xmlns="http://www.w3.org/2000/svg" aria-label="Happy Holidays gift sticker with to and from lines">
  <defs>
    <linearGradient id="gold-foil" x1="0" y1="0" x2="1" y2="1">
      <stop offset="0" stop-color="var(--gold-light)"/>
      <stop offset="0.45" stop-color="var(--gold-mid)"/>
      <stop offset="1" stop-color="var(--gold-deep)"/>
    </linearGradient>
    <radialGradient id="red-field" cx="0.5" cy="0.5" r="0.6">
      <stop offset="0.4" stop-color="var(--red-glow)"/>
      <stop offset="1" stop-color="var(--red-deep)"/>
    </radialGradient>
  </defs>

  <!-- die cut outline, gold foil -->
  <path class="sticker__foil" fill="url(#gold-foil)"
        d="M612 148 C720 148 805 185 855 232 Q855 335 950 340 L950 808 Q855 812 855 918 C800 965 700 996 612 996 C524 996 424 965 369 918 Q369 812 274 808 L274 340 Q369 335 369 232 C419 185 504 148 612 148 Z"/>

  <!-- red field with ornamental wreath area -->
  <path class="sticker__field" fill="url(#red-field)" stroke="var(--rope)" stroke-width="10"
        role="img" aria-label="Gold mistletoe wreath and white berry sprigs on red"
        d="M612 172 C714 172 792 206 836 248 Q840 348 928 356 L928 792 Q840 800 836 902 C786 944 698 972 612 972 C526 972 438 944 388 902 Q384 800 296 792 L296 356 Q384 348 388 248 C432 206 510 172 612 172 Z"/>

  <!-- white label disc -->
  <circle class="sticker__label" cx="608" cy="584" r="248" fill="var(--label-white)"/>

  <!-- greeting -->
  <text class="sticker__title" x="618" y="480" text-anchor="middle" font-size="96" textLength="300" lengthAdjust="spacingAndGlyphs">Happy</text>
  <text class="sticker__title" x="618" y="592" text-anchor="middle" font-size="100" textLength="388" lengthAdjust="spacingAndGlyphs">Holidays</text>

  <!-- write-in fields -->
  <text class="sticker__field-label" x="436" y="676" font-size="62">from:</text>
  <line class="sticker__rule" x1="432" y1="686" x2="778" y2="686"/>
  <text class="sticker__field-label" x="468" y="744" font-size="58">to:</text>
  <line class="sticker__rule" x1="468" y1="758" x2="728" y2="758"/>
</svg>
</body>
</html>
```